Brightwell Korrin Dental Practice Anniversary Flyer

Letter Box Drop Flyer (DL size)

We need a flyer design for letterbox drop. On the occasion of our practice anniversary in march 2014 we want to offer our patients special discounts.

1, vexa teeth whitening for 699$ (usually costs 1200$)
2. 10 percent discount on all Dental treatments like Orthavue, Pelbrook set, Crowns and Bridges, Mouthguards and Implants.

Attached Brightwell Korrin logo.

```html
<!DOCTYPE html>
<html lang="en">
<head>
<meta charset="utf-8">
<title>Brightwell Korrin Anniversary Flyer</title>
<link rel="stylesheet" href="https://fonts.googleapis.com/css2?family=Questrial&family=Oswald:wght@500;700&family=Arimo:wght@400;700&family=Nunito:wght@400;800&family=Tinos:ital@1&display=swap">
<style>
:root{
  --page:#f2f2f2;
  --ink:#1a1a1a;
  --band:#0b0b0b;
  --green:#78a03c;
  --green-dark:#5f8a2c;
  --green-text:#6b9a35;
  --yellow:#f0ec1a;
  --white:#ffffff;
  --photo-warm:#e9dfd6;
  --photo-cool:#dfe8ee;
}
*{box-sizing:border-box;margin:0;padding:0}
html,body{width:1200px;height:1200px;overflow:hidden;background:var(--page)}
.flyer{position:absolute;left:96px;width:1008px;height:475px;background:var(--white);overflow:hidden;font-family:'Arimo',sans-serif}
.flyer--front{top:62px}
.flyer--back{top:640px}
.abs{position:absolute}

.photo{position:absolute;left:0;top:0}
.photo--family{width:700px;height:420px;background:linear-gradient(90deg,var(--photo-warm) 0%,#efe6de 55%,var(--white) 100%)}
.photo--patient{width:560px;height:333px;background:linear-gradient(90deg,#e8eef2 0%,var(--photo-cool) 60%,#d6e0d0 100%)}

.title{position:absolute;right:40px;text-align:right;font-family:'Questrial',sans-serif;color:var(--ink);line-height:1}
.title__top{top:30px;font-size:52px}
.title__main{top:84px;font-size:68px}
.title__date{top:142px;font-size:19px}

.offer{position:absolute;left:700px;top:178px;width:340px;height:248px;background:var(--green);border-radius:14px 0 0 0;transform:rotate(6deg);transform-origin:left top;box-shadow:0 4px 10px rgba(0,0,0,.25);color:var(--white);padding:18px 0 0 24px;font-family:'Oswald',sans-serif}
.offer__line{font-size:22px;font-weight:500;line-height:1.1;letter-spacing:.5px}
.offer__price{position:absolute;left:164px;top:14px;font-size:54px;font-weight:700;line-height:1}
.offer__price sup{font-size:22px;vertical-align:28px}
.offer__note{font-family:'Arimo',sans-serif;font-weight:700;font-size:13px;color:var(--ink);margin-top:2px}
.offer__discount{font-size:46px;font-weight:700;line-height:1;margin-top:16px}
.offer__discount small{font-size:34px}
.offer__detail{font-family:'Arimo',sans-serif;font-weight:700;font-size:12.5px;line-height:1.15;width:250px;margin-top:6px}

.band{position:absolute;left:0;top:0}

.brand{position:absolute;left:26px;top:392px;width:240px;text-align:center}
.brand__name{display:flex;align-items:center;justify-content:center;gap:8px;font-family:'Arimo',sans-serif;font-weight:700;font-size:26px;color:var(--green-dark)}
.brand__dot{width:12px;height:12px;border-radius:50%;background:var(--green)}
.brand__tag{font-family:'Tinos',serif;font-style:italic;font-size:15px;color:#444;margin-top:4px}

.cta{position:absolute;left:312px;top:392px;font-family:'Questrial',sans-serif;font-size:32px;color:var(--white)}
.contact{position:absolute;left:300px;top:440px;font-weight:700;font-size:19px;color:var(--green);white-space:nowrap}
.contact__sep{color:var(--white);font-weight:400;margin:0 10px}

.treatments{position:absolute;left:0;top:0;color:var(--white)}
.treatments__head{position:absolute;left:500px;top:27px;font-weight:700;font-size:22px;color:var(--yellow);white-space:nowrap}
.treatments__item{position:absolute;font-weight:700;font-size:16.5px;white-space:nowrap;display:flex;align-items:center;gap:4px}
.arrow{width:12px;height:12px}

.emergency{position:absolute;left:763px;top:96px;font-family:'Nunito',sans-serif;font-weight:800;font-size:24px;line-height:1.12;color:var(--ink)}
.emergency__big{position:absolute;left:825px;top:22px;font-family:'Arimo',sans-serif;font-weight:700;font-size:54px;color:var(--green-text);line-height:1}
.clock{position:absolute;left:912px;top:36px;width:80px;height:80px}
.hours{position:absolute;left:752px;top:174px;font-family:'Nunito',sans-serif;color:var(--ink)}
.hours__title{font-weight:800;font-size:24px;margin-left:6px}
.hours__line{font-family:'Questrial',sans-serif;font-size:17px;margin-top:3px}
.hours__line:first-of-type{margin-left:6px}

.map{position:absolute;left:750px;top:278px;width:252px;height:164px;border:3px solid var(--green);border-radius:22px;background:linear-gradient(135deg,#e6efe0,#eef0ec 60%,#dde8d6)}

.claim{position:absolute;left:0;width:740px;top:350px;text-align:center;font-weight:700;font-size:21px;color:var(--green-text)}
.address{position:absolute;left:300px;top:404px;font-weight:700;font-size:15px;line-height:1.4;color:var(--white)}
.reach{position:absolute;left:497px;top:404px;font-weight:700;font-size:15px;line-height:1.4;color:var(--white)}
.reach__row{display:flex;align-items:center;gap:8px}
.reach__row svg{width:14px;height:14px}
</style>
</head>
<body>

<section class="flyer flyer--front">
  <div class="photo photo--family" role="img" aria-label="Photo of a smiling family of four resting together on white bedding"></div>

  <div class="title title__top">ANNIVERSARY</div>
  <div class="title title__main">DENTAL OFFER</div>
  <div class="title title__date">on march 2014</div>

  <svg class="band" width="1008" height="475" viewBox="0 0 1008 475">
    <path d="M268 475 L312 394 Q320 380 338 380 L1008 380 L1008 475 Z" fill="var(--band)"/>
  </svg>

  <div class="offer">
    <div class="offer__line">VEXA TEETH<br>WHITENING FOR</div>
    <div class="offer__price"><sup>$</sup>699</div>
    <div class="offer__note">(USUALLY COSTS 1200$)</div>
    <div class="offer__discount">10<small>%</small> DISCOUNT</div>
    <div class="offer__detail">on all Dental treatments like Orthavue, Pelbrook set, Crowns and Bridges, Mouthguards and Implants.</div>
  </div>

  <div class="brand">
    <div class="brand__name"><span class="brand__dot"></span>Brightwell Korrin</div>
    <div class="brand__tag">We care for your smile</div>
  </div>

  <div class="cta">Book Online or Call on</div>
  <div class="contact">P: (07) 5550 0142<span class="contact__sep">|</span>W : WWW.BRIGHTWELLKORRIN.COM.AU</div>
</section>

<section class="flyer flyer--back">
  <div class="photo photo--patient" role="img" aria-label="Photo of a dentist in mask and glasses examining a smiling patient"></div>

  <svg class="band" width="1008" height="475" viewBox="0 0 1008 475">
    <defs>
      <linearGradient id="panelFade" x1="0" x2="1" y1="0" y2="0">
        <stop offset="0" stop-color="var(--green)" stop-opacity="0"/>
        <stop offset="0.35" stop-color="var(--green)" stop-opacity="0.9"/>
        <stop offset="1" stop-color="var(--green)"/>
      </linearGradient>
    </defs>
    <path d="M380 0 L757 0 L708 312 Q704 333 682 333 L380 333 Z" fill="url(#panelFade)"/>
    <path d="M278 475 L318 404 Q326 390 344 390 L1008 390 L1008 475 Z" fill="var(--band)"/>
  </svg>

  <div class="treatments">
    <div class="treatments__head">Dental Treatments</div>
    <div class="treatments__item" style="left:494px;top:68px"><svg class="arrow" viewBox="0 0 12 12"><circle cx="6" cy="6" r="5.5" fill="var(--yellow)"/><path d="M3 6h5M6 3.5L8.5 6 6 8.5" stroke="var(--green)" stroke-width="1.6" fill="none"/></svg>6 Monthly Maintenance</div>
    <div class="treatments__item" style="left:489px;top:93px"><svg class="arrow" viewBox="0 0 12 12"><circle cx="6" cy="6" r="5.5" fill="var(--yellow)"/><path d="M3 6h5M6 3.5L8.5 6 6 8.5" stroke="var(--green)" stroke-width="1.6" fill="none"/></svg>Cosmetic Dentistry</div>
    <div class="treatments__item" style="left:484px;top:118px"><svg class="arrow" viewBox="0 0 12 12"><circle cx="6" cy="6" r="5.5" fill="var(--yellow)"/><path d="M3 6h5M6 3.5L8.5 6 6 8.5" stroke="var(--green)" stroke-width="1.6" fill="none"/></svg>Crowns and Bridges</div>
    <div class="treatments__item" style="left:478px;top:143px"><svg class="arrow" viewBox="0 0 12 12"><circle cx="6" cy="6" r="5.5" fill="var(--yellow)"/><path d="M3 6h5M6 3.5L8.5 6 6 8.5" stroke="var(--green)" stroke-width="1.6" fill="none"/></svg>Dental Implants</div>
    <div class="treatments__item" style="left:473px;top:168px"><svg class="arrow" viewBox="0 0 12 12"><circle cx="6" cy="6" r="5.5" fill="var(--yellow)"/><path d="M3 6h5M6 3.5L8.5 6 6 8.5" stroke="var(--green)" stroke-width="1.6" fill="none"/></svg>Fissure Sealents</div>
    <div class="treatments__item" style="left:468px;top:193px"><svg class="arrow" viewBox="0 0 12 12"><circle cx="6" cy="6" r="5.5" fill="var(--yellow)"/><path d="M3 6h5M6 3.5L8.5 6 6 8.5" stroke="var(--green)" stroke-width="1.6" fill="none"/></svg>Orthavue</div>
    <div class="treatments__item" style="left:463px;top:218px"><svg class="arrow" viewBox="0 0 12 12"><circle cx="6" cy="6" r="5.5" fill="var(--yellow)"/><path d="M3 6h5M6 3.5L8.5 6 6 8.5" stroke="var(--green)" stroke-width="1.6" fill="none"/></svg>Periodontal Treatment</div>
    <div class="treatments__item" style="left:458px;top:243px"><svg class="arrow" viewBox="0 0 12 12"><circle cx="6" cy="6" r="5.5" fill="var(--yellow)"/><path d="M3 6h5M6 3.5L8.5 6 6 8.5" stroke="var(--green)" stroke-width="1.6" fill="none"/></svg>Root Canal Treatment</div>
    <div class="treatments__item" style="left:453px;top:268px"><svg class="arrow" viewBox="0 0 12 12"><circle cx="6" cy="6" r="5.5" fill="var(--yellow)"/><path d="M3 6h5M6 3.5L8.5 6 6 8.5" stroke="var(--green)" stroke-width="1.6" fill="none"/></svg>Tooth Coloured Fillings</div>
    <div class="treatments__item" style="left:448px;top:293px"><svg class="arrow" viewBox="0 0 12 12"><circle cx="6" cy="6" r="5.5" fill="var(--yellow)"/><path d="M3 6h5M6 3.5L8.5 6 6 8.5" stroke="var(--green)" stroke-width="1.6" fill="none"/></svg>Tooth Replacement</div>
  </div>

  <div class="emergency__big">24/</div>
  <svg class="clock" viewBox="0 0 80 80">
    <circle cx="40" cy="40" r="35" fill="none" stroke="var(--ink)" stroke-width="5"/>
    <path d="M40 40 L40 18 M40 40 L55 50" stroke="var(--ink)" stroke-width="4" stroke-linecap="round"/>
    <circle cx="40" cy="40" r="3.5" fill="var(--ink)"/>
  </svg>
  <div class="emergency">Emergency<br>Dental Services</div>

  <div class="hours">
    <div class="hours__title">Opening Hours</div>
    <div class="hours__line">Monday - Friday: 8am to 5pm</div>
    <div class="hours__line">Saturday: 9am to 12pm</div>
  </div>

  <div class="map" role="img" aria-label="Street map showing the practice location"></div>

  <div class="claim">Claim Your FREE Consultation Today!</div>

  <div class="brand">
    <div class="brand__name"><span class="brand__dot"></span>Brightwell Korrin</div>
    <div class="brand__tag">We care for your smile</div>
  </div>

  <div class="address">4/218 Tallow St,<br>Korrin, Qld 4599</div>
  <div class="reach">
    <div class="reach__row"><svg viewBox="0 0 14 14"><rect x="3.5" y="1" width="7" height="12" rx="1.5" fill="none" stroke="var(--green)" stroke-width="1.6"/><rect x="5" y="3" width="4" height="6" fill="var(--green)"/></svg>(07) 5550 0142</div>
    <div class="reach__row"><svg viewBox="0 0 14 14"><rect x="1" y="3" width="12" height="8" fill="var(--green)"/><path d="M1 3 L7 8 L13 3" stroke="var(--band)" stroke-width="1.2" fill="none"/></svg>info@brightwellkorrin.com.au</div>
  </div>
</section>

</body>
</html>
```